Automotive eCommerce Business looking for a business card design

Looking for a clean and simple business card design. Our company name is "Harbor Crest Auto" and we are a company specializing in the ecommerce sales of automotive parts, specifically for pick up trucks and large SUVs. Our company colours are red, black, and white.

Feel free to use the logo provided or create a new logo that you seem fit. Looking forward to your creative ideas!

Industry/Entity Type

Automotive

Contact Information for Business Card

We were thinking of a possibly two-sided design featuring just the logo and company name on one side, and personal information on the other side. Single sided designs will be considered as well.

Font styles to use
Serif
Sans Serif
Decorative

Colors
ec1f27
ffffff
000000

Requirements
Must have
• Space for employee's name, title, phone number and email address, along with the company address and website somewhere.

```html
<!DOCTYPE html>
<html lang="en">
<head>
<meta charset="utf-8">
<title>Harbor Crest Auto – Business Card</title>
<link href="https://fonts.googleapis.com/css2?family=Exo+2:wght@400;500;600&family=Open+Sans:wght@400;600&display=swap" rel="stylesheet">
<style>
  :root {
    --brand-red: #ec1f27;
    --ink: #000000;
    --paper: #ffffff;
    --stage: #111111;
    --card-dark: #141414;
    --text-dark: #1a1a1a;
    --text-muted: #333333;
  }
  * { margin: 0; padding: 0; box-sizing: border-box; }
  html, body {
    width: 1200px; height: 1000px; overflow: hidden;
    background: var(--stage);
  }
  .stage {
    position: relative; width: 1200px; height: 1000px;
  }
  .card {
    position: absolute; top: 350px;
    width: 520px; height: 300px;
    border-radius: 22px; overflow: hidden;
  }

  /* Front: personal details */
  .card-front { left: 55px; background: var(--paper); }
  .card-front .base-band {
    position: absolute; left: 0; right: 0; bottom: 0; height: 40px;
    background: linear-gradient(180deg, #f0262e, #d91920);
  }
  .person { position: absolute; left: 36px; top: 38px; }
  .person-name {
    font-family: "Exo 2", sans-serif; font-weight: 500;
    font-size: 22px; letter-spacing: 1px; color: var(--brand-red);
    text-transform: uppercase; line-height: 1;
  }
  .person-title {
    font-family: "Open Sans", sans-serif; font-size: 13px;
    color: var(--text-muted); margin-top: 4px;
  }
  .contact-list {
    position: absolute; left: 36px; top: 128px; list-style: none;
    font-family: "Open Sans", sans-serif; font-size: 13px; color: var(--text-dark);
  }
  .contact-list li { display: flex; align-items: center; gap: 8px; height: 19px; }
  .contact-list svg { width: 11px; height: 11px; fill: var(--brand-red); flex: none; }

  .brand-pin { position: absolute; left: 330px; top: 40px; width: 170px; }
  .brand-mark {
    display: flex; align-items: center; gap: 8px;
  }
  .brand-dot {
    width: 22px; height: 22px; border-radius: 50%; background: var(--brand-red); flex: none;
  }
  .brand-name {
    font-family: "Exo 2", sans-serif; font-weight: 600; font-size: 17px;
    color: var(--brand-red); line-height: 1.1; text-transform: uppercase;
  }
  .pin-stem {
    position: absolute; left: 62px; width: 8px; background: var(--ink);
  }
  .pin-stem.upper { top: 68px; height: 60px; }
  .pin-stem.lower { top: 192px; height: 14px; }
  .address {
    position: absolute; left: 46px; top: 136px;
    font-family: "Open Sans", sans-serif; font-weight: 600; font-size: 13px;
    color: var(--text-dark); line-height: 1.3;
  }

  /* Back: brand side */
  .card-back {
    left: 625px; background: var(--card-dark);
    display: flex; flex-direction: column; align-items: center; justify-content: center;
    gap: 22px;
  }
  .back-square {
    width: 84px; height: 84px; border-radius: 14px; background: var(--brand-red);
  }
  .back-name {
    font-family: "Exo 2", sans-serif; font-weight: 400; font-size: 21px;
    letter-spacing: 3px; color: var(--paper); text-transform: uppercase;
  }
</style>
</head>
<body>
<main class="stage">
  <section class="card card-front" aria-label="Business card front">
    <div class="person">
      <p class="person-name">Lorem Ipsum</p>
      <p class="person-title">Owner</p>
    </div>
    <ul class="contact-list">
      <li>
        <svg viewBox="0 0 24 24" aria-hidden="true"><path d="M6.6 10.8a15 15 0 0 0 6.6 6.6l2.2-2.2c.3-.3.7-.4 1-.2 1.1.4 2.3.6 3.6.6.6 0 1 .4 1 1V20c0 .6-.4 1-1 1A17 17 0 0 1 3 4c0-.6.4-1 1-1h3.5c.6 0 1 .4 1 1 0 1.3.2 2.5.6 3.6.1.3 0 .7-.2 1z"/></svg>
        +12 3456 7890
      </li>
      <li>
        <svg viewBox="0 0 24 24" aria-hidden="true"><path d="M2 5h20v14H2z M2 5l10 8 10-8" /></svg>
        yourmailaddress.com
      </li>
      <li>
        <svg viewBox="0 0 24 24" aria-hidden="true"><circle cx="12" cy="12" r="10"/></svg>
        www.yourwebsite.com
      </li>
    </ul>
    <div class="brand-pin">
      <div class="brand-mark">
        <span class="brand-dot"></span>
        <span class="brand-name">Harbor Crest Auto</span>
      </div>
      <span class="pin-stem upper"></span>
      <p class="address">Street name<br>zip code, city</p>
      <span class="pin-stem lower"></span>
    </div>
    <div class="base-band"></div>
  </section>

  <section class="card card-back" aria-label="Business card back">
    <span class="back-square"></span>
    <p class="back-name">Harbor Crest Auto Ltd</p>
  </section>
</main>
</body>
</html>
```